I'm looking for a fresh new design for my business Leonard Fasque Creative.
I am a photographer and videographer.
The card must be easy to print, eye catching and easy to read. It must reflect the fact that I work in a creative area, but not so edgy as to scare away my corporate clients.
Sub text should read Photography, Video, Design
There also needs to be room for phone number and email.

```html
<!DOCTYPE html>
<html lang="en">
<head>
<meta charset="utf-8">
<title>Leonard Fasque Creative – Business Card</title>
<link href="https://fonts.googleapis.com/css2?family=Tinos&display=swap" rel="stylesheet">
<style>
  :root {
    --page-bg: #ece7df;
    --card-bg: #ffffff;
    --ink: #111111;
    --accent-blue: #3347a3;
  }
  html, body {
    margin: 0;
    padding: 0;
    width: 1200px;
    height: 1200px;
    overflow: hidden;
    background: var(--page-bg);
  }
  .canvas {
    position: relative;
    width: 1200px;
    height: 1200px;
  }
  .business-card {
    position: absolute;
    left: 100px;
    top: 320px;
    width: 1000px;
    height: 560px;
    background: var(--card-bg);
    box-shadow: 0 6px 24px rgba(0,0,0,0.15);
    overflow: hidden;
    font-family: "Tinos", "Times New Roman", serif;
    color: var(--ink);
  }
  .identity {
    position: absolute;
    left: 60px;
    top: 210px;
  }
  .identity__name,
  .identity__role {
    margin: 0;
    font-size: 46px;
    font-weight: 400;
    line-height: 1.15;
  }
  .initial { color: var(--accent-blue); }
  .identity__services {
    margin: 14px 0 0;
    font-size: 34px;
    line-height: 1.2;
  }
  .contact {
    position: absolute;
    left: 60px;
    bottom: 40px;
    font-size: 26px;
    line-height: 1.25;
  }
  .contact p { margin: 0; }
  .contact__phone { font-size: 32px; }
  .contact__web { margin-top: 14px !important; }
  .brand-mark {
    position: absolute;
    right: 60px;
    top: 40px;
    display: flex;
    align-items: center;
    gap: 18px;
  }
  .brand-mark__name {
    font-size: 30px;
    color: var(--ink);
  }
</style>
</head>
<body>
<div class="canvas">
  <article class="business-card">
    <div class="brand-mark">
      <svg width="64" height="64" viewBox="0 0 64 64" aria-hidden="true">
        <circle cx="32" cy="32" r="26" fill="none" stroke="var(--ink)" stroke-width="8"/>
      </svg>
      <span class="brand-mark__name">Leonard Fasque Creative</span>
    </div>

    <header class="identity">
      <h1 class="identity__name"><span class="initial">L</span>eonard <span class="initial">F</span>asque</h1>
      <p class="identity__role"><span class="initial">C</span>reative</p>
      <p class="identity__services">Photography,Video,Design</p>
    </header>

    <footer class="contact">
      <p class="contact__email">hello@fasquestudio.com</p>
      <p class="contact__phone">555014273</p>
      <p class="contact__web">www.fasquestudio.com</p>
    </footer>
  </article>
</div>
</body>
</html>
```